T.R.L (Tidal Resonance Lifting) is a form of energy healing that raises the vibration of the DNA so that it releases old energy patterns that no longer serve you. This allows the body to remember its natural ability to heal itself perfectly.

The energy is called in telepathically from the Acturians, the dolphins, the platinum ray and the Octahedron.

I would like a logo that incorporates all of these moadlities.

I will also require help with setting up my facebook page and website but until these are setup I cannot include the details so space will need to be saved for this on the business card

Target Market(s)

Alternative health

Industry/Entity Type

Business

Logo Text

T.R.L

Requirements
Must have
• Colors of the platinum ray. I have drafted the below as to what I would like it to say on it:-

Business Card –
Front:-
Taking you to a higher vibration
Mabel Thornby
Tidal Resonance Lifting Facilitator
www.quorvintel.example
+(61) 412 735 289 mabelthornby4471@quorvintel.example

Back:-
Appointments
For:-
Date: Time:
Location:

```html
<!DOCTYPE html>
<html lang="en">
<head>
<meta charset="utf-8">
<title>T.R.L Business Card</title>
<link rel="stylesheet" href="https://fonts.googleapis.com/css2?family=Marcellus&family=Arimo:wght@400&display=swap">
<style>
  :root {
    --page-bg: #ebebeb;
    --card-bg: #35b0e6;
    --card-shadow: rgba(0, 0, 0, 0.28);
    --text-light: #ffffff;
    --accent-purple: #8a5ca8;
    --glow: rgba(255, 255, 255, 0.85);
  }
  * { margin: 0; padding: 0; box-sizing: border-box; }
  html, body {
    width: 1200px;
    height: 900px;
    overflow: hidden;
    background: var(--page-bg);
  }
  .business-card {
    position: absolute;
    left: 95px;
    top: 122px;
    width: 991px;
    height: 538px;
    background: var(--card-bg);
    box-shadow: 0 2px 4px var(--card-shadow);
    color: var(--text-light);
  }
  .brand-mark {
    position: absolute;
    left: 50px;
    top: 90px;
    width: 175px;
    height: 175px;
    border-radius: 50%;
    background: var(--accent-purple);
    box-shadow: 0 0 24px 8px var(--glow);
    display: flex;
    align-items: center;
    justify-content: center;
  }
  .brand-mark__name {
    font-family: "Marcellus", serif;
    font-size: 40px;
    color: var(--text-light);
    letter-spacing: 1px;
  }
  .headline {
    position: absolute;
    left: 180px;
    right: 0;
    text-align: center;
    font-family: "Marcellus", serif;
    color: var(--text-light);
  }
  .headline--initials { top: 28px; font-size: 40px; }
  .headline--tagline { top: 85px; font-size: 45px; }
  .divider {
    position: absolute;
    left: 265px;
    top: 175px;
    width: 690px;
    height: 6px;
    border-radius: 3px;
    background: linear-gradient(90deg, rgba(255,255,255,0) 0%, var(--glow) 18%, #ffffff 50%, var(--glow) 82%, rgba(255,255,255,0) 100%);
    box-shadow: 0 0 8px var(--glow);
  }
  .person {
    position: absolute;
    left: 180px;
    right: 0;
    text-align: center;
    font-family: "Arimo", Arial, sans-serif;
  }
  .person--name { top: 215px; font-size: 36px; }
  .person--role { top: 274px; font-size: 30px; }
  .contact-list {
    position: absolute;
    left: 0;
    top: 355px;
    width: 100%;
    list-style: none;
    font-family: "Arimo", Arial, sans-serif;
    font-size: 24px;
  }
  .contact-list__item {
    position: relative;
    height: 56px;
  }
  .contact-list__icon {
    position: absolute;
    left: 362px;
    top: 0;
    width: 28px;
    height: 28px;
  }
  .contact-list__text {
    position: absolute;
    left: 395px;
    right: 10px;
    top: 0;
    text-align: center;
  }
</style>
</head>
<body>
  <section class="business-card">
    <div class="brand-mark"><span class="brand-mark__name">T.R.L</span></div>

    <h1 class="headline headline--initials">T.R.L.</h1>
    <p class="headline headline--tagline">Taking You to A Higher Vibration</p>
    <div class="divider"></div>

    <h2 class="person person--name" style="font-weight:400">Mabel Thornby</h2>
    <p class="person person--role">Tidal Resonance Lifting Facilitator</p>

    <ul class="contact-list">
      <li class="contact-list__item">
        <svg class="contact-list__icon" viewBox="0 0 24 24" aria-hidden="true">
          <path fill="var(--accent-purple)" d="M6.6 2.5c.6-.3 1.3 0 1.6.6l1.6 3.4c.3.6.1 1.2-.4 1.6l-1.5 1.1c.9 2.3 2.6 4.5 4.7 5.9l1.3-1.3c.5-.5 1.2-.6 1.8-.2l3.1 2c.6.4.8 1.1.4 1.7l-1.2 2c-.5.8-1.5 1.2-2.4.9C9.4 18.6 5 13.4 4.3 6.7c-.1-.9.4-1.8 1.2-2.2z"/>
        </svg>
        <span class="contact-list__text">+(61) 412 735 289</span>
      </li>
      <li class="contact-list__item">
        <svg class="contact-list__icon" viewBox="0 0 24 24" aria-hidden="true">
          <rect x="2.5" y="5.5" width="19" height="13" fill="none" stroke="var(--accent-purple)" stroke-width="1.6"/>
          <path d="M2.5 5.5l9.5 7 9.5-7M2.5 18.5l7-6M21.5 18.5l-7-6" fill="none" stroke="var(--accent-purple)" stroke-width="1.4"/>
        </svg>
        <span class="contact-list__text">mabelthornby4471@quorvintel.example</span>
      </li>
      <li class="contact-list__item">
        <svg class="contact-list__icon" viewBox="0 0 24 24" aria-hidden="true">
          <circle cx="12" cy="12" r="9" fill="var(--accent-purple)"/>
          <path d="M12 3v18M3 12h18M5.5 7.5h13M5.5 16.5h13" stroke="var(--card-bg)" stroke-width="1.2" fill="none"/>
          <ellipse cx="12" cy="12" rx="4" ry="9" fill="none" stroke="var(--card-bg)" stroke-width="1.2"/>
        </svg>
        <span class="contact-list__text">www.quorvintel.example</span>
      </li>
    </ul>
  </section>
</body>
</html>
```